TK & LJ Shearing Pty Ltd

We already have an existing logo created by Lumen Guild however we have restructured to a company. We would like someone to add Pty Ltd to our business name please.

Colors

Designer to choose only greyscale colors for use in the design.

```html
<!DOCTYPE html>
<html lang="en">
<head>
<meta charset="utf-8">
<title>TK &amp; LJ Shearing Pty Ltd – Business Card</title>
<link rel="stylesheet" href="https://fonts.googleapis.com/css2?family=Roboto+Slab:wght@700&family=Lato:wght@400;900&display=swap">
<style>
  :root {
    --bg: #e2e2e2;
    --ink: #0b0b0b;
    --paper: #ffffff;
    --sheep-tone: #dadada;
    --text: #1a1a1a;
    --shadow: rgba(0,0,0,0.22);
  }
  html, body {
    margin: 0;
    width: 1200px;
    height: 900px;
    overflow: hidden;
    background: var(--bg);
  }
  .stage { position: relative; width: 1200px; height: 900px; }

  .card {
    position: absolute;
    width: 540px;
    height: 309px;
    box-shadow: 0 10px 26px var(--shadow);
    overflow: hidden;
  }
  .card-front { left: 80px; top: 140px; background: var(--ink); }
  .card-back  { left: 580px; top: 440px; background: var(--paper); }

  .brand {
    position: absolute;
    left: 0; right: 0; top: 50%;
    transform: translateY(-50%);
    display: flex;
    align-items: center;
    justify-content: center;
    gap: 14px;
  }
  .brand-dot {
    width: 34px; height: 34px;
    border-radius: 50%;
    background: var(--paper);
  }
  .brand-name {
    font-family: "Roboto Slab", serif;
    font-weight: 700;
    font-size: 30px;
    color: var(--paper);
    letter-spacing: 1px;
    text-transform: uppercase;
  }

  .sheep-art {
    position: absolute;
    right: 20px;
    top: 18px;
    width: 230px;
    height: 275px;
  }

  .holders {
    position: absolute;
    left: 30px;
    top: 150px;
    font-family: "Lato", sans-serif;
    font-weight: 900;
    font-size: 17px;
    line-height: 1.2;
    color: var(--text);
    text-transform: uppercase;
    letter-spacing: 0.3px;
  }
  .contacts {
    position: absolute;
    left: 30px;
    top: 205px;
    margin: 0; padding: 0;
    list-style: none;
    font-family: "Lato", sans-serif;
    font-size: 15px;
    color: var(--text);
  }
  .contacts li {
    display: flex;
    align-items: center;
    gap: 8px;
    height: 26px;
  }
  .contact-icon { width: 20px; height: 20px; flex: none; }
</style>
</head>
<body>
<main class="stage">
  <section class="card card-front" aria-label="Card front">
    <div class="brand">
      <span class="brand-dot"></span>
      <span class="brand-name">TK &amp; LJ Shearing Pty Ltd</span>
    </div>
  </section>

  <section class="card card-back" aria-label="Card back">
    <svg class="sheep-art" role="img" aria-label="Faint grey illustration of a standing sheep" viewBox="0 0 230 275">
      <defs>
        <radialGradient id="sheepTone" cx="50%" cy="45%" r="60%">
          <stop offset="0%" stop-color="#d6d6d6"/>
          <stop offset="100%" stop-color="#e6e6e6"/>
        </radialGradient>
      </defs>
      <rect x="0" y="0" width="230" height="275" rx="60" fill="url(#sheepTone)"/>
    </svg>

    <div class="holders">
      <div class="holder">Tom Kerrigan</div>
      <div class="holder">Lena Jarvis</div>
    </div>

    <ul class="contacts">
      <li>
        <svg class="contact-icon" viewBox="0 0 20 20" aria-hidden="true">
          <circle cx="10" cy="10" r="10" fill="var(--ink)"/>
          <path d="M6.5 5.5l2 0.3 0.8 2.2-1.2 1a6 6 0 0 0 2.9 2.9l1-1.2 2.2 0.8 0.3 2c-4.8 0.8-8.8-3.2-8-8z" fill="#fff"/>
        </svg>
        <span>041 5550192</span>
      </li>
      <li>
        <svg class="contact-icon" viewBox="0 0 20 20" aria-hidden="true">
          <circle cx="10" cy="10" r="10" fill="var(--ink)"/>
          <rect x="5" y="6.5" width="10" height="7" fill="#fff"/>
          <path d="M5 6.5l5 4 5-4" fill="none" stroke="var(--ink)" stroke-width="1"/>
        </svg>
        <span>tkljshearing@fleecepost.com</span>
      </li>
      <li>
        <svg class="contact-icon" viewBox="0 0 20 20" aria-hidden="true">
          <circle cx="10" cy="10" r="10" fill="var(--ink)"/>
          <path d="M10 4.5a3.5 3.5 0 0 1 3.5 3.5c0 2.6-3.5 7-3.5 7s-3.5-4.4-3.5-7A3.5 3.5 0 0 1 10 4.5z" fill="#fff"/>
          <circle cx="10" cy="8" r="1.3" fill="var(--ink)"/>
        </svg>
        <span>PO Box 418 Kelmore WA 6590</span>
      </li>
    </ul>
  </section>
</main>
</body>
</html>
```